Cobaltine Pilates Summer Promotions

I would like to create 2 x A6 one-side flyers for my Cobaltine Pilates private yoga summer promotions. I have 2 promotions available (bring a friend for free + 4 for price of 3 package). I would like the 2 flyers to look similar in style but would like them to look different enough so they catch the eye of the customer that there are 2 different promotions available.
Attached is my PowerPoint "versions" which I created myself but would like them to be taken to the next level for professionalism and design. You do not have to follow this layout - this was just my (non-designer-mind) ideas.
The wording in the PowerPoint must be included. You are free to use all my logos and images attached in whichever way you think works best. Feel free to use other yoga/scenic imagery you find which may be suitable.

Please stick to these font options:
Logo font: Amatic
Main text font: Raleway

Colour palette in the branding guidelines attached.

Font styles to use
Other font styles liked:
• Amatic + Raleway

Requirements
Must have
• Colour palette as per attached branding guidelines
• Fonts Amatic + Raleway
• Same design style but 2 different layouts for the 2 different promotions
• My logo must be included
• Call to action to book a session
• Wording as per PowerPoint attached
• Contact details - email, phone and website
Nice to have
• Optional other relevant yoga/lavender themed imagery
• Picture of me (to build familiarity with customers)

```html
<!DOCTYPE html>
<html lang="en">
<head>
<meta charset="utf-8">
<title>Cobaltine Pilates – Summer Promotions</title>
<link href="https://fonts.googleapis.com/css2?family=Amatic+SC:wght@400;700&family=Raleway:wght@400;500;600&display=swap" rel="stylesheet">
<style>
:root{
  --stage:#5b5c5f;
  --paper:#ffffff;
  --lavender:#9d80a8;
  --lavender-soft:#b49cbc;
  --lavender-pale:#e9e1ec;
  --ink:#555258;
  --ink-soft:#6d6970;
  --photo-light:#f1eeee;
  --photo-mid:#d9cfd6;
}
*{margin:0;padding:0;box-sizing:border-box}
html,body{width:1200px;height:874px;overflow:hidden;background:var(--stage)}
body{position:relative;font-family:'Raleway',sans-serif;color:var(--ink)}
.flyer{position:absolute;top:53px;width:547px;height:769px;background:var(--paper);overflow:hidden;box-shadow:0 2px 10px rgba(0,0,0,.35)}
.flyer--friend{left:38px}
.flyer--package{left:618px;width:545px}
.abs{position:absolute}
.photo{position:absolute;left:0;top:0;width:100%}
.flyer--friend .photo{height:370px;background:linear-gradient(180deg,var(--photo-light) 0%,#e8dfe2 45%,#efe9ec 80%,var(--paper) 100%)}
.flyer--package .photo{height:270px;background:linear-gradient(180deg,var(--photo-light) 0%,#e6dee2 60%,var(--paper) 100%)}
.portrait{position:absolute;left:414px;top:395px;width:131px;height:300px;background:linear-gradient(90deg,rgba(255,255,255,1) 0%,rgba(222,210,220,.7) 45%,rgba(205,190,205,.6) 100%)}
.brand{position:absolute;font-family:'Amatic SC',sans-serif;font-weight:400;color:var(--ink-soft);font-size:40px;letter-spacing:1px;line-height:1}
.brand-mark{position:absolute;width:10px;height:10px;border-radius:50%;background:var(--lavender)}
.title-band{position:absolute;background:var(--lavender);opacity:.92;border-radius:4px 28px 28px 4px}
.title{position:absolute;font-family:'Amatic SC',sans-serif;font-weight:400;color:#fff;line-height:1;white-space:nowrap}
.headline{position:absolute;color:var(--lavender);font-weight:500;white-space:nowrap}
.body-copy{position:absolute;font-size:12px;line-height:18.5px;color:var(--ink)}
.body-copy p+p{margin-top:18.5px}
.tab{position:absolute;height:25px;background:var(--lavender);color:#fff;font-weight:600;font-size:12.5px;line-height:25px;padding-left:6px;clip-path:polygon(0 0,100% 0,93% 50%,100% 100%,0 100%)}
.tab-text{position:absolute;font-size:12px;line-height:16.5px;color:var(--ink)}
.price{position:absolute;text-align:left;color:var(--ink)}
.price .label{font-size:14px}
.price .amount{font-size:31px;color:var(--lavender);font-weight:500;line-height:1.05}
.price .note{font-size:13px}
.price--center{text-align:center;width:150px}
.divider{position:absolute;width:1px;background:var(--lavender-soft)}
.cta-band{position:absolute;background:var(--lavender);border-radius:30px 6px 6px 30px;opacity:.9}
.cta{position:absolute;font-family:'Amatic SC',sans-serif;color:#fff;font-size:32px;line-height:32px;text-align:center;white-space:nowrap}
.footer{position:absolute;left:0;bottom:0;width:100%;height:48px;background:var(--lavender);color:#fff;display:flex;align-items:center;justify-content:space-between;padding:0 14px 0 28px}
.footer .item{display:flex;align-items:center;gap:6px;font-size:12px}
.footer .phone{font-size:15px;font-weight:600}
.footer svg{width:14px;height:14px;fill:none;stroke:#fff;stroke-width:1.6}
</style>
</head>
<body>

<!-- Flyer 1: Bring a friend for free -->
<section class="flyer flyer--friend">
  <div class="photo" role="img" aria-label="Instructor smiling in a balancing yoga pose in a bright white studio with candles and a small statue"></div>

  <span class="brand-mark" style="left:60px;top:60px"></span>
  <div class="brand" style="left:26px;top:88px">Cobaltine Pilates</div>

  <div class="title-band" style="left:0;top:283px;width:290px;height:64px"></div>
  <div class="title" style="left:28px;top:292px;font-size:42px">Private Yoga Classes</div>

  <div class="headline" style="left:29px;top:360px;font-size:22px">Bring a friend for free</div>

  <div class="body-copy" style="left:29px;top:393px;width:320px">
    <p>Going to a new yoga class can be a little intimidating. Where do I put my mat? Does it matter I can't even touch my toes? What language will they speak? I get it. I've been there.</p>
    <p>So instead, how about trying private yoga classes? We can practice at the best time for your schedule. And make it even more fun by doing it with your friend.</p>
    <p>This summer if you book a private class with me you can now do just that, and bring a friend along for free!</p>
  </div>

  <div class="tab" style="left:362px;top:386px;width:148px">Offer period</div>
  <div class="tab-text" style="left:367px;top:417px">July to September 2017</div>
  <div class="tab" style="left:362px;top:451px;width:148px">Location</div>
  <div class="tab-text" style="left:367px;top:483px;width:140px">Let's discuss! I have options to use studio spaces or we can do it at yours' or your friend's home</div>

  <div class="price" style="left:28px;top:618px"><div class="label">60 minutes</div><div class="amount">120fr</div><div class="note">(60fr each!)</div></div>
  <div class="divider" style="left:117px;top:616px;height:76px"></div>
  <div class="price" style="left:126px;top:618px"><div class="label">75 minutes</div><div class="amount">150fr</div><div class="note">(70fr each!)</div></div>
  <div class="divider" style="left:214px;top:616px;height:76px"></div>
  <div class="price" style="left:224px;top:618px"><div class="label">90 minutes</div><div class="amount">180fr</div><div class="note">(90fr each!)</div></div>

  <div class="cta-band" style="left:320px;top:612px;width:227px;height:86px"></div>
  <div class="cta" style="left:320px;top:622px;width:227px">Get in touch to<br>book your session!</div>

  <footer class="footer">
    <span class="item phone"><svg viewBox="0 0 24 24"><path d="M5 3h4l2 5-2.5 1.5a11 11 0 0 0 6 6L16 13l5 2v4a2 2 0 0 1-2 2A16 16 0 0 1 3 5a2 2 0 0 1 2-2z"/></svg>0712 555 018</span>
    <span class="item"><svg viewBox="0 0 24 24"><circle cx="12" cy="12" r="9"/><path d="M3 12h18M12 3c3 3 3 15 0 18M12 3c-3 3-3 15 0 18"/></svg>www.cobaltine.studio</span>
    <span class="item"><svg viewBox="0 0 24 24"><rect x="3" y="5" width="18" height="14" rx="1"/><path d="M3 6l9 7 9-7"/></svg>hello@cobaltine.studio</span>
  </footer>
</section>

<!-- Flyer 2: 4 classes for the price of 3 -->
<section class="flyer flyer--package">
  <div class="photo" role="img" aria-label="Instructor seated in prayer pose beside a window in a bright white studio"></div>
  <div class="portrait" role="img" aria-label="Faded portrait of the instructor with hands in prayer position"></div>

  <span class="brand-mark" style="left:56px;top:56px"></span>
  <div class="brand" style="left:22px;top:84px">Cobaltine Pilates</div>

  <div class="title-band" style="left:110px;top:163px;width:304px;height:54px;border-radius:26px"></div>
  <div class="title" style="left:110px;top:168px;width:304px;text-align:center;font-size:40px">Private Yoga Classes</div>

  <div class="headline" style="left:0;top:222px;width:545px;text-align:center;font-size:21px">4 classes for the price of 3</div>

  <div class="body-copy" style="left:60px;top:253px;width:425px;text-align:center;font-size:13.6px;line-height:20px">
    <p>Would you like to develop a home yoga practice? Do you have a particular yoga pose or series of poses you'd like to work on? Or perhaps you'd just like an opportunity to ask questions and dive deeper into your yoga practice?</p>
    <p>Private classes are the perfect way to do this! And this summer Cobaltine Pilates is offering a private class package to help you really make the most of your yoga practice.</p>
    <p>During July to September 2017, if you book 3 private yoga classes you will get the 4th for free!</p>
  </div>

  <div class="price price--center" style="left:35px;top:494px"><div class="label">60 minute package</div><div class="amount">360fr</div><div class="note">(save 120fr)</div></div>
  <div class="divider" style="left:190px;top:488px;height:76px"></div>
  <div class="price price--center" style="left:198px;top:494px"><div class="label">75 minute package</div><div class="amount">450fr</div><div class="note">(save 150fr)</div></div>
  <div class="divider" style="left:353px;top:488px;height:76px"></div>
  <div class="price price--center" style="left:361px;top:494px"><div class="label">90 minute package</div><div class="amount">540fr</div><div class="note">(save 180fr)</div></div>

  <div class="tab" style="left:16px;top:587px;width:148px">Offer period</div>
  <div class="tab-text" style="left:21px;top:619px">July to September 2017</div>
  <div class="tab" style="left:16px;top:649px;width:148px">Location</div>
  <div class="tab-text" style="left:21px;top:681px;width:300px">Let's discuss! I have options to use studio spaces or we can do it at yours' or your friend's home</div>

  <div class="cta-band" style="left:318px;top:623px;width:227px;height:80px"></div>
  <div class="cta" style="left:318px;top:630px;width:227px">Get in touch to<br>book your session!</div>

  <footer class="footer">
    <span class="item phone"><svg viewBox="0 0 24 24"><path d="M5 3h4l2 5-2.5 1.5a11 11 0 0 0 6 6L16 13l5 2v4a2 2 0 0 1-2 2A16 16 0 0 1 3 5a2 2 0 0 1 2-2z"/></svg>0712 555 018</span>
    <span class="item"><svg viewBox="0 0 24 24"><circle cx="12" cy="12" r="9"/><path d="M3 12h18M12 3c3 3 3 15 0 18M12 3c-3 3-3 15 0 18"/></svg>www.cobaltine.studio</span>
    <span class="item"><svg viewBox="0 0 24 24"><rect x="3" y="5" width="18" height="14" rx="1"/><path d="M3 6l9 7 9-7"/></svg>hello@cobaltine.studio</span>
  </footer>
</section>

</body>
</html>
```